Business Card Design

We have our logo and everything in place. Looking to have a layout for our new business cards designed. These will be printed with a matte finish, possibly rounded corners, and looking to incorporate some cool spot UV layers into the design.

Ive uploaded the existing card front and back as well as our logo.

Card Size Will Be 3.5" x 2"

```html
<!DOCTYPE html>
<html lang="en">
<head>
<meta charset="utf-8">
<title>Oakridge Deck and Rail – Business Cards</title>
<link rel="stylesheet" href="https://fonts.googleapis.com/css2?family=Libre+Baskerville:wght@400;700&display=swap">
<style>
  :root {
    --page-bg: #2a2a2b;
    --card-bg: #353334;
    --card-edge: #4a4849;
    --spot-uv: #1b1a1b;
    --text-light: #f4f4f4;
    --accent-blue: #1e9be0;
  }
  * { box-sizing: border-box; margin: 0; padding: 0; }
  html, body {
    width: 1200px;
    height: 900px;
    overflow: hidden;
    background: var(--page-bg);
    font-family: "Libre Baskerville", Georgia, serif;
  }
  .sheet {
    width: 1200px;
    height: 900px;
    display: flex;
    flex-direction: column;
    align-items: center;
    justify-content: center;
    gap: 56px;
  }
  .card {
    position: relative;
    width: 560px;
    height: 320px;
    border-radius: 28px;
    background: var(--card-bg);
    border: 1px solid var(--card-edge);
    box-shadow: 0 10px 24px rgba(0,0,0,0.45);
  }
  .wordmark {
    color: var(--spot-uv);
    font-weight: 400;
    line-height: 1.1;
    text-align: center;
  }
  .card-front {
    display: flex;
    align-items: center;
    justify-content: center;
  }
  .card-front .wordmark { font-size: 40px; }
  .card-front .wordmark span { display: block; font-size: 20px; letter-spacing: 0.18em; text-transform: uppercase; margin-top: 10px; }
  .card-back .wordmark {
    position: absolute;
    left: 34px;
    top: 110px;
    width: 250px;
    font-size: 38px;
  }
  .card-back .wordmark span { display: block; font-size: 17px; letter-spacing: 0.16em; text-transform: uppercase; margin-top: 10px; }
  .contact {
    position: absolute;
    left: 300px;
    top: 92px;
    color: var(--text-light);
  }
  .contact-name {
    font-size: 17px;
    font-weight: 700;
    letter-spacing: 0.08em;
    text-transform: uppercase;
  }
  .contact-role {
    color: var(--accent-blue);
    font-size: 15px;
    font-weight: 700;
    margin: 2px 0 14px 10px;
  }
  .contact-line {
    font-size: 11.5px;
    line-height: 1.4;
    margin-left: 14px;
  }
  .contact-web {
    font-size: 13.5px;
    margin: 30px 0 0 30px;
  }
</style>
</head>
<body>
  <main class="sheet">
    <section class="card card-front" aria-label="Card front">
      <div class="wordmark">Oakridge<span>Deck and Rail</span></div>
    </section>
    <section class="card card-back" aria-label="Card back">
      <div class="wordmark">Oakridge<span>Deck and Rail</span></div>
      <div class="contact">
        <p class="contact-name">Daniel Mercer</p>
        <p class="contact-role">President</p>
        <p class="contact-line">555.014.2290</p>
        <p class="contact-line">oakridgedeckandrail@example.com</p>
        <p class="contact-web">www.oakridgedeckandrail.com</p>
      </div>
    </section>
  </main>
</body>
</html>
```